Innovative Strategic IT Solutions and Management Consulting

Looking for a fresh design idea to represent a company which specializes in innovative strategic IT solutions focusing on information assurance, enterprise content management, health information technology, web applications, strategic IT solutions and solutions architect.

KOVL...the company name means "new beginning" in Greek or the acronym for Keen-Option-Venture-Logic. We pride ourselves in understanding the client's business and needs before proposing an innovative solutions.

Innovation / Secure / Strategy - the core motto

Color: Maroon / Burgundy / Silver / White / Grey / Black

Primary focus color: Burgundy / Silver

```html
<!DOCTYPE html>
<html lang="en">
<head>
<meta charset="utf-8">
<title>KOVL – Innovation | Security | Strategy</title>
<link href="https://fonts.googleapis.com/css2?family=Oxygen:wght@300;400&display=swap" rel="stylesheet">
<style>
:root{
  --burgundy:#9e1535;
  --burgundy-deep:#5a1420;
  --maroon:#4a0f18;
  --silver:#c4c4c4;
  --grey-text:#8a8a8a;
  --panel:#f5f5f5;
  --key-bg:#e6e6e6;
  --white:#ffffff;
}
*{margin:0;padding:0;box-sizing:border-box}
html,body{width:1200px;height:1115px;overflow:hidden;background:var(--white)}
body{font-family:"Oxygen",sans-serif;position:relative}
.site-header{position:absolute;top:0;left:0;width:1200px;height:110px;background:var(--white)}
.brand{position:absolute;left:196px;top:14px;display:flex;align-items:center;gap:14px}
.brand-name{font-weight:300;font-size:60px;color:var(--burgundy);letter-spacing:1px;line-height:1}
.brand-mark{width:62px;height:62px;border:2px solid var(--burgundy);border-radius:50%}
.tagline{position:absolute;left:472px;top:34px;font-weight:300;font-size:26px;color:var(--grey-text)}
.contact{position:absolute;left:858px;top:24px;list-style:none}
.contact li{display:flex;align-items:center;gap:14px;height:31px;font-size:19px;color:var(--grey-text);font-weight:300}
.contact svg{width:26px;height:26px}
.main-nav{position:absolute;top:110px;left:0;width:1200px;height:43px;background:linear-gradient(#6b2a36,#5a2431);border-top:6px solid var(--burgundy)}
.main-nav a{position:absolute;top:6px;color:var(--white);text-decoration:none;font-size:19px}
.main-nav .active{left:201px;top:0;width:117px;height:37px;background:var(--burgundy);text-align:center;line-height:30px}
.hero{position:absolute;top:153px;left:0;width:1200px;height:348px;background:linear-gradient(100deg,#2a1418 0%,#6a2a3a 40%,#8a4a58 60%,#c9c4c6 100%)}
.hero-rule{position:absolute;left:208px;top:60px;width:237px;height:2px;background:var(--burgundy)}
.key-links{position:absolute;top:501px;left:0;width:1200px;height:167px;background:var(--white)}
.key-panel{position:absolute;left:156px;top:10px;width:878px;height:147px;background:var(--panel)}
.key-rule{position:absolute;left:193px;width:808px;height:2px;background:var(--burgundy)}
.key-item{position:absolute;top:45px;width:176px;height:77px;background:var(--key-bg);border:1px solid #a04a60;color:var(--burgundy);font-size:24px;line-height:24px;text-align:center;display:flex;align-items:center;justify-content:center;text-decoration:none}
.key-arrow{position:absolute;top:44px;width:35px;height:78px;background:#d4d4d4;display:flex;align-items:center;justify-content:center}
.ticker{position:absolute;top:668px;left:0;width:1200px;height:48px;background:var(--burgundy)}
.ticker-btn{position:absolute;top:7px;width:34px;height:34px;border:2px solid var(--white);border-radius:50%;display:flex;align-items:center;justify-content:center}
.ticker-text{position:absolute;left:410px;top:12px;color:var(--white);font-size:21px}
.services{position:absolute;top:716px;left:0;width:1200px;height:344px;background:linear-gradient(160deg,#5a1520,#4a1019 50%,#7a1628)}
.service-ring{position:absolute;top:48px;width:170px;height:170px;border:2px solid var(--white);border-radius:50%;display:flex;align-items:center;justify-content:center}
.service-title{position:absolute;top:250px;width:320px;margin-left:-160px;text-align:center;color:var(--white);font-weight:400;font-size:22px;line-height:30px}
.site-footer{position:absolute;top:1060px;left:0;width:1200px;height:55px;background:var(--maroon);color:var(--white);font-size:17px;font-weight:300;padding:18px 0 0 198px}
</style>
</head>
<body>
<header class="site-header">
  <div class="brand"><span class="brand-name">kovl</span><span class="brand-mark"></span></div>
  <p class="tagline">Innovation | Security | Strategy</p>
  <ul class="contact">
    <li><svg viewBox="0 0 26 26"><circle cx="13" cy="13" r="13" fill="#9e1535"/><path d="M9 7l3 3-2 2c1 2 2 3 4 4l2-2 3 3-2 2c-5 0-10-5-10-10z" fill="#fff"/></svg>01632 960 418</li>
    <li><svg viewBox="0 0 26 26"><circle cx="13" cy="13" r="13" fill="#9e1535"/><rect x="7" y="9" width="12" height="9" fill="none" stroke="#fff" stroke-width="1.5"/><path d="M7 9l6 5 6-5" fill="none" stroke="#fff" stroke-width="1.5"/></svg>hello@kovl.example</li>
  </ul>
</header>
<nav class="main-nav">
  <a class="active" href="#">Home</a>
  <a href="#" style="left:377px">Menuitem1</a>
  <a href="#" style="left:537px">Menuitem2</a>
  <a href="#" style="left:678px">Menuitem3</a>
  <a href="#" style="left:831px">Menuitem4</a>
</nav>
<section class="hero" role="img" aria-label="Hand touching a glowing touchscreen tile among floating silver panels">
  <div class="hero-rule"></div>
</section>
<section class="key-links">
  <div class="key-panel"></div>
  <div class="key-rule" style="top:30px"></div>
  <div class="key-rule" style="top:136px"></div>
  <div class="key-arrow" style="left:196px"><svg width="24" height="24" viewBox="0 0 24 24"><circle cx="12" cy="12" r="12" fill="#9e1535"/><path d="M14 7l-5 5 5 5" fill="none" stroke="#fff" stroke-width="2.5"/></svg></div>
  <a class="key-item" href="#" style="left:252px">key item<br>one link</a>
  <a class="key-item" href="#" style="left:446px">key item<br>two link</a>
  <a class="key-item" href="#" style="left:637px">key item<br>three link</a>
  <a class="key-item" href="#" style="left:826px">key item<br>four link</a>
  <div class="key-arrow" style="left:1021px"><svg width="24" height="24" viewBox="0 0 24 24"><circle cx="12" cy="12" r="12" fill="#9e1535"/><path d="M10 7l5 5-5 5" fill="none" stroke="#fff" stroke-width="2.5"/></svg></div>
</section>
<section class="ticker">
  <span class="ticker-btn" style="left:288px"></span>
  <span class="ticker-btn" style="left:328px"><svg width="14" height="18" viewBox="0 0 14 18"><path d="M10 2L4 9l6 7" fill="none" stroke="#fff" stroke-width="2"/></svg></span>
  <p class="ticker-text">Social feed item one etc lorum ipsim dolore</p>
  <span class="ticker-btn" style="left:957px"><svg width="14" height="18" viewBox="0 0 14 18"><path d="M4 2l6 7-6 7" fill="none" stroke="#fff" stroke-width="2"/></svg></span>
</section>
<section class="services">
  <div class="service-ring" style="left:200px"><svg width="104" height="92" viewBox="0 0 104 92" fill="#bdbdbd"><rect x="8" y="2" width="36" height="86"/><rect x="48" y="20" width="22" height="68"/><rect x="72" y="28" width="24" height="60"/><rect x="0" y="88" width="104" height="4"/><g fill="#6a1a28"><rect x="16" y="12" width="2" height="72"/><rect x="22" y="12" width="2" height="72"/><rect x="28" y="12" width="2" height="72"/><rect x="56" y="30" width="2" height="54"/><rect x="62" y="30" width="2" height="54"/><rect x="80" y="38" width="2" height="46"/><rect x="86" y="38" width="2" height="46"/></g></svg></div>
  <h2 class="service-title" style="left:277px">Enterprise Content<br>Management</h2>

  <div class="service-ring" style="left:437px"><svg width="124" height="90" viewBox="0 0 124 90" fill="none" stroke="#bdbdbd"><circle cx="44" cy="45" r="30" stroke-width="12" stroke-dasharray="8 6"/><circle cx="44" cy="45" r="24" stroke-width="5"/><circle cx="44" cy="45" r="12" stroke-width="4"/><circle cx="102" cy="58" r="14" stroke-width="6" stroke-dasharray="4 3"/><circle cx="102" cy="58" r="6" stroke-width="3"/></svg></div>
  <h2 class="service-title" style="left:518px;top:244px">Web<br>Applications</h2>

  <div class="service-ring" style="left:674px"><svg width="100" height="88" viewBox="0 0 100 88"><path d="M50 88L8 46C-6 30 4 2 26 2c11 0 19 7 24 14C55 9 63 2 74 2c22 0 32 28 18 44z" fill="#bdbdbd"/><circle cx="56" cy="24" r="6" fill="#6a1a28"/><path d="M52 36l-8 28h8l8-28z" fill="#6a1a28"/></svg></div>
  <h2 class="service-title" style="left:763px">Health<br>Information Technology</h2>

  <div class="service-ring" style="left:912px"><svg width="80" height="80" viewBox="0 0 80 80" fill="none" stroke="#bdbdbd" stroke-width="11"><path d="M10 36A30 30 0 0 1 64 22"/><path d="M70 44A30 30 0 0 1 16 58"/><path d="M56 4h16v18z" fill="#bdbdbd" stroke="none"/><path d="M24 76H8V58z" fill="#bdbdbd" stroke="none"/></svg></div>
  <h2 class="service-title" style="left:1005px">Solutions<br>Architect</h2>
</section>
<footer class="site-footer">Company Registration number.&nbsp;&nbsp; Copyright 2014. Address line 1&nbsp; Address line 2&nbsp;&nbsp; Address line 3</footer>
</body>
</html>
```